Gadri Management - Managing Urban Projects for the City of Modiin

Gadri Management needs a website that projects its professionalism and innovation to the residents of the city of Modiin. The design needs include: 1) a homepage design, 2) ~12 customized icons used on the homepage, 3) a layered image (city landscape with company logo on it) used as a fullwidth background image on the homepage. The client wants a site that is pleasant on the eye and easy to navigate. The client wants the site to project the organization as being professional and innovative.

Target Market(s)

adult residents of the city of modiin, israel

Industry/Entity Type

management of urban projects

Number of Pages Required

1 page

Font styles to use
Sans Serif

Requirements
Must have
• psd of design and psd of main fullwidth background image on the homepage
Nice to have
• icons for navigation bar and homepage teasers
Should not have
• colors should match the logo attached, font should be modern

```html
<!DOCTYPE html>
<html lang="he" dir="rtl">
<head>
<meta charset="utf-8">
<title>Gadri Management</title>
<link href="https://fonts.googleapis.com/css2?family=Heebo:wght@400;500;700;800&display=swap" rel="stylesheet">
<style>
:root{
  --green:#4cb648;
  --green-dark:#3fa13b;
  --mint:#edfcec;
  --ink:#1f1f1f;
  --text:#3a3a3a;
  --muted:#8a8a8a;
  --line:#dedede;
  --white:#ffffff;
  --footer:#2b2a28;
}
*{margin:0;padding:0;box-sizing:border-box}
html,body{width:1200px;height:3116px;overflow:hidden}
body{font-family:'Heebo',sans-serif;color:var(--text);background:var(--white);position:relative;direction:rtl}
.abs{position:absolute}
.btn{position:absolute;background:var(--green);color:var(--white);font-weight:700;font-size:17px;border-radius:7px;display:flex;align-items:center;justify-content:center}

/* hero */
.hero{position:absolute;left:0;top:0;width:1200px;height:565px;overflow:hidden;
  background:linear-gradient(180deg,#3b3f3a 0%,#4d5a44 40%,#566a41 65%,#3f4d3a 100%)}
.hero-photo{position:absolute;inset:0;background:radial-gradient(ellipse at 55% 75%,rgba(70,110,130,.55),transparent 35%),radial-gradient(ellipse at 30% 70%,rgba(90,130,60,.5),transparent 45%)}
.hero-shade{position:absolute;inset:0;background:rgba(20,20,20,.35)}
.brand{position:absolute;right:160px;top:48px;display:flex;align-items:center;gap:8px;color:var(--white);font-weight:700;font-size:17px}
.brand .dot{width:26px;height:26px;border-radius:50%;background:var(--green)}
.hero-title{position:absolute;right:208px;top:212px;color:var(--white);font-size:31px;font-weight:800;white-space:nowrap}
.hero-text{position:absolute;right:208px;top:264px;width:470px;color:var(--white);font-size:14px;line-height:26px}
.sidebar{position:absolute;left:1059px;top:0;width:141px;height:565px;background:var(--green)}
.nav-item{position:absolute;left:8px;width:126px;height:58px;display:flex;align-items:center;gap:8px;padding-right:10px;border-bottom:1px solid rgba(255,255,255,.3);color:var(--white);font-size:11px;white-space:nowrap}
.nav-item:last-child{border-bottom:none}
.nav-icon{width:30px;height:30px;border:1.5px solid var(--white);border-radius:50%;display:flex;align-items:center;justify-content:center;flex:none}
.scroll-tab{position:absolute;left:553px;top:538px}

/* teaser cards */
.card{position:absolute;top:650px;width:218px;height:216px;border-radius:18px;background:var(--mint);text-align:center}
.card svg{position:absolute;left:69px;top:50px}
.card span{position:absolute;left:0;right:0;top:140px;font-size:17px;font-weight:700;color:var(--ink)}

/* about */
.about-title{position:absolute;right:146px;top:1128px;font-size:29px;font-weight:800;color:var(--ink)}
.about-text{position:absolute;right:146px;top:1180px;width:362px;font-size:13.5px;line-height:26px}
.panel{position:absolute}
.play{position:absolute;left:352px;top:1245px;width:70px;height:70px;border-radius:50%;background:rgba(40,40,40,.55);display:flex;align-items:center;justify-content:center}
.play div{width:52px;height:52px;border-radius:50%;background:var(--green);display:flex;align-items:center;justify-content:center}

/* gallery */
.gallery{position:absolute;left:0;top:1652px;width:1200px;height:465px;background:linear-gradient(180deg,#4fbb4b 0%,#49b345 70%,#53b44c 100%)}
.gallery h2{position:absolute;left:0;right:0;top:64px;text-align:center;color:var(--white);font-size:35px;font-weight:800}
.shot{position:absolute;top:160px;width:218px;height:218px;border:5px solid var(--white);border-radius:18px}
.arrow{position:absolute;top:255px}

/* contact */
.eyebrow{position:absolute;right:143px;top:2190px;color:var(--green);font-size:21px}
.contact-title{position:absolute;right:143px;top:2222px;font-size:37px;font-weight:800;color:var(--ink)}
.contact-text{position:absolute;right:143px;top:2282px;width:400px;font-size:12px;line-height:22px}
.info{position:absolute;right:143px;display:flex;align-items:center;gap:18px}
.info-icon{width:40px;height:40px;border-radius:50%;background:var(--green);display:flex;align-items:center;justify-content:center;flex:none}
.info b{display:block;font-size:13px;color:var(--ink)}
.info small{display:block;font-size:12px;color:var(--text);margin-top:4px}
.field{position:absolute;height:50px;border:1.5px solid var(--line);border-radius:8px;font-size:12px;color:var(--muted);padding:16px 18px}

/* footer */
.footer{position:absolute;left:0;top:2668px;width:1200px;height:390px;background:linear-gradient(180deg,#2f2c29,#262522)}
.footer h3{position:absolute;color:var(--white);font-size:25px;font-weight:700;white-space:nowrap}
.foot-brand{position:absolute;right:143px;top:80px;display:flex;align-items:center;gap:8px;color:var(--white);font-weight:700;font-size:16px}
.foot-brand .dot{width:24px;height:24px;border-radius:50%;background:var(--green)}
.foot-text{position:absolute;right:143px;top:198px;width:340px;color:var(--white);font-size:12px;line-height:26px}
.foot-link{position:absolute;color:var(--white);font-size:12px;font-weight:700;white-space:nowrap}
.foot-info{position:absolute;right:835px;display:flex;align-items:center;gap:18px;color:var(--white);white-space:nowrap}
.foot-info b{display:block;font-size:13px}
.foot-info small{display:block;font-size:12px;margin-top:4px}
.bar{position:absolute;left:0;top:3058px;width:1200px;height:58px;background:var(--green)}
.copy{position:absolute;right:143px;top:16px;color:var(--white);font-size:20px}
.social{position:absolute;top:13px;width:32px;height:32px;border-radius:50%;background:var(--white)}
</style>
</head>
<body>

<section class="hero">
  <div class="hero-photo" role="img" aria-label="Aerial view of a city with a park and lake"></div>
  <div class="hero-shade"></div>
  <div class="brand"><span>Gadri Management</span><span class="dot"></span></div>
  <h1 class="hero-title">גדרי ניהול פרויקטים עירוניים</h1>
  <p class="hero-text">טקסט זה הוא טקסט דמה המשמש להמחשת מבנה הפסקה באזור הפתיחה של האתר, עד שיסופק התוכן הסופי. הוא נועד להציג את אורך השורות ואת קצב הקריאה בעמוד, ואינו מתאר פרויקט אמיתי. התוכן יוחלף בהמשך בהסבר קצר על פעילות החברה, על ניהול הפרויקטים העירוניים ועל השירות לתושבים</p>
  <div class="btn" style="left:866px;top:395px;width:126px;height:45px">צור קשר</div>

  <nav class="sidebar">
    <div class="nav-item" style="top:20px"><span class="nav-icon"><svg width="16" height="16" viewBox="0 0 16 16" fill="none" stroke="#fff" stroke-width="1.4"><path d="M2 8l6-5 6 5M4 7v7h8V7"/></svg></span><span>בית</span></div>
    <div class="nav-item" style="top:78px"><span class="nav-icon"><svg width="16" height="16" viewBox="0 0 16 16" fill="none" stroke="#fff" stroke-width="1.4"><circle cx="8" cy="5" r="3"/><path d="M2 15c1-4 11-4 12 0"/></svg></span><span>אודות</span></div>
    <div class="nav-item" style="top:136px"><span class="nav-icon"><svg width="16" height="16" viewBox="0 0 16 16" fill="none" stroke="#fff" stroke-width="1.4"><rect x="2" y="6" width="5" height="8"/><rect x="9" y="2" width="5" height="12"/></svg></span><span>מיזמי פיתוח</span></div>
    <div class="nav-item" style="top:194px"><span class="nav-icon"><svg width="16" height="16" viewBox="0 0 16 16" fill="none" stroke="#fff" stroke-width="1.4"><circle cx="8" cy="8" r="5"/><path d="M8 5v3l2 2"/></svg></span><span>פרויקטים</span></div>
    <div class="nav-item" style="top:252px"><span class="nav-icon"><svg width="16" height="16" viewBox="0 0 16 16" fill="none" stroke="#fff" stroke-width="1.4"><circle cx="8" cy="8" r="3"/><path d="M8 1v3M8 12v3M1 8h3M12 8h3"/></svg></span><span>עדכונים</span></div>
    <div class="nav-item" style="top:310px"><span class="nav-icon"><svg width="16" height="16" viewBox="0 0 16 16" fill="none" stroke="#fff" stroke-width="1.4"><path d="M3 13l7-7M8 3l5 5M6 5l5 5"/></svg></span><span>מכרזים</span></div>
    <div class="nav-item" style="top:368px"><span class="nav-icon"><svg width="16" height="16" viewBox="0 0 16 16" fill="none" stroke="#fff" stroke-width="1.4"><rect x="3" y="2" width="10" height="12"/><path d="M5 5h6M5 8h6M5 11h6"/></svg></span><span>מוסדות ציבור</span></div>
    <div class="nav-item" style="top:426px"><span class="nav-icon"><svg width="16" height="16" viewBox="0 0 16 16" fill="none" stroke="#fff" stroke-width="1.4"><rect x="2" y="3" width="12" height="10" rx="2"/><path d="M3 12l4-4 3 3 2-2 2 2"/></svg></span><span>גלריה</span></div>
    <div class="nav-item" style="top:484px"><span class="nav-icon"><svg width="16" height="16" viewBox="0 0 16 16" fill="none" stroke="#fff" stroke-width="1.4"><path d="M4 2l2 3-1.5 1.5c1 2 2.5 3.5 4.5 4.5L10.5 9.5l3 2-1 2.5C7 14 2 9 2 3.5z"/></svg></span><span>צור קשר</span></div>
  </nav>
</section>

<svg class="scroll-tab abs" width="94" height="64" viewBox="0 0 94 64">
  <polygon points="0,0 94,0 47,62" fill="#fff"/>
  <path d="M38 12l9 8 9-8M38 21l9 8 9-8" fill="none" stroke="#4cb648" stroke-width="2.5"/>
</svg>

<!-- teaser cards -->
<div class="card" style="left:141px">
  <svg width="80" height="80" viewBox="0 0 80 80" fill="none" stroke="#222" stroke-width="2"><rect x="14" y="30" width="20" height="26" rx="2"/><path d="M19 30v-6a5 5 0 0110 0v6"/><rect x="46" y="34" width="20" height="26" rx="2"/><path d="M51 34v-6a5 5 0 0110 0v6"/><path d="M40 12v56"/></svg>
  <span>מרכז קניות</span>
</div>
<div class="card" style="left:374px">
  <svg width="80" height="80" viewBox="0 0 80 80" fill="none" stroke="#222" stroke-width="2"><rect x="16" y="10" width="48" height="54" rx="6"/><path d="M16 40h48M22 18h36v16H22zM10 18h6M64 18h6"/><circle cx="26" cy="52" r="4"/><circle cx="54" cy="52" r="4"/><path d="M22 64v6h8v-6M50 64v6h8v-6"/></svg>
  <span>מרכז התחבורה</span>
</div>
<div class="card" style="left:608px">
  <svg width="80" height="80" viewBox="0 0 80 80" fill="none" stroke="#222" stroke-width="2"><rect x="12" y="24" width="10" height="32" rx="4"/><rect x="22" y="18" width="10" height="44" rx="4"/><rect x="58" y="24" width="10" height="32" rx="4"/><rect x="48" y="18" width="10" height="44" rx="4"/><path d="M32 40h16M4 40h8M68 40h8"/></svg>
  <span>מרכז הספורט העירוני</span>
</div>
<div class="card" style="left:841px">
  <svg width="80" height="80" viewBox="0 0 80 80" fill="none" stroke="#222" stroke-width="2"><path d="M4 20c10-8 20-8 30 0s20 8 30 0"/><ellipse cx="18" cy="46" rx="9" ry="14"/><path d="M18 46v24"/><rect x="38" y="52" width="34" height="6"/><path d="M40 58v12M70 58v12M40 44h30v8"/></svg>
  <span>פארק הענב</span>
</div>

<!-- about -->
<svg class="panel" style="left:141px;top:1020px" width="500" height="550" viewBox="0 0 500 550">
  <defs>
    <linearGradient id="cityA" x1="0" y1="0" x2="0" y2="1"><stop offset="0" stop-color="#a9b6c4"/><stop offset=".5" stop-color="#9c8e84"/><stop offset=".8" stop-color="#8e5a4a"/><stop offset="1" stop-color="#5d6d5a"/></linearGradient>
    <linearGradient id="cityB" x1="0" y1="0" x2="0" y2="1"><stop offset="0" stop-color="#b7c4d2"/><stop offset=".45" stop-color="#a79a8e"/><stop offset=".7" stop-color="#9a5644"/><stop offset="1" stop-color="#4f6b48"/></linearGradient>
  </defs>
  <path role="img" aria-label="Aerial view of city towers and red-roofed buildings" d="M14 40 L226 2 Q240 0 240 14 L240 510 L0 548 L0 56 Q0 42 14 40Z" fill="url(#cityA)"/>
  <path role="img" aria-label="Aerial view of a school campus with a sports field" d="M257 -68 L484 -8 Q499 -4 499 12 L499 548 L268 498 Q257 496 257 484Z" fill="url(#cityB)"/>
</svg>
<div class="play"><div><svg width="20" height="22" viewBox="0 0 20 22"><polygon points="2,1 19,11 2,21" fill="#fff"/></svg></div></div>

<h2 class="about-title">עלינו</h2>
<p class="about-text">טקסט זה הוא טקסט דמה המשמש להמחשת אזור התוכן על אודות החברה. הוא נועד להראות את מבנה הפסקה, את אורך השורות ואת המרווחים בין הטקסט לתמונות שלצידו. בהמשך יוחלף בתיאור של תחומי הפעילות, של צוות הניהול ושל הפרויקטים העירוניים שהחברה מלווה מתכנון ועד מסירה. הטקסט אינו מתאר עובדות אמיתיות ונועד לתצוגה בלבד, עד שהלקוח יספק את התוכן הסופי לעמוד</p>
<div class="btn" style="left:938px;top:1406px;width:116px;height:46px">קרא עוד</div>

<!-- gallery -->
<section class="gallery">
  <h2>מצגת של פרויקטים</h2>
  <div class="shot" style="left:141px;background:linear-gradient(180deg,#6d8a6e,#9fc43a 55%,#3e7a3a)" role="img" aria-label="Aerial view of a canal lined with trees"></div>
  <div class="shot" style="left:374px;background:linear-gradient(180deg,#5f7d55,#7a9468 50%,#4f6f8a)" role="img" aria-label="Aerial view of a landscaped civic plaza"></div>
  <div class="shot" style="left:608px;background:linear-gradient(180deg,#6f7c86,#8a7a6e 50%,#3a3a3e)" role="img" aria-label="Aerial view of a construction site beside a road"></div>
  <div class="shot" style="left:841px;background:linear-gradient(180deg,#8aa2b8,#3a8fc9 50%,#5e8a5a)" role="img" aria-label="Aerial view of a lake surrounded by housing"></div>
  <svg class="arrow" style="left:90px" width="22" height="34" viewBox="0 0 22 34"><path d="M18 3L5 17l13 14" fill="none" stroke="rgba(255,255,255,.6)" stroke-width="3"/></svg>
  <svg class="arrow" style="left:1088px" width="22" height="34" viewBox="0 0 22 34"><path d="M4 3l13 14L4 31" fill="none" stroke="#fff" stroke-width="3"/></svg>
</section>

<!-- contact -->
<p class="eyebrow">להשאיר לנו קשר</p>
<h2 class="contact-title">נהיה בקשר</h2>
<p class="contact-text">טקסט זה הוא טקסט דמה המזמין את התושבים לפנות אל החברה בכל שאלה. הוא נועד להמחיש את אורך הפסקה באזור יצירת הקשר, ויוחלף בהמשך בתוכן הסופי שיספק הלקוח, כולל שעות פעילות ודרכי פנייה נוספות</p>

<div class="info" style="top:2380px"><span class="info-icon"><svg width="18" height="18" viewBox="0 0 16 16" fill="#fff"><path d="M4 1.5l2.2 3.2-1.6 1.5c1 2 2.6 3.6 4.6 4.6l1.5-1.6 3.2 2.2-1 2.6C7 14 2 9 1.5 2.5z"/></svg></span><div><b>התקשר אלינו</b><small>08-9000123</small></div></div>
<div class="info" style="top:2456px"><span class="info-icon"><svg width="16" height="20" viewBox="0 0 16 20" fill="#fff"><path d="M8 0a7 7 0 017 7c0 5-7 13-7 13S1 12 1 7a7 7 0 017-7zm0 4a3 3 0 100 6 3 3 0 000-6z"/></svg></span><div><b>כתובת</b><small>רחוב הדוגמה 12, עיר האלון</small></div></div>
<div class="info" style="top:2524px"><span class="info-icon"><svg width="18" height="14" viewBox="0 0 18 14" fill="#fff"><rect width="18" height="14" rx="2"/><path d="M1 2l8 6 8-6" stroke="#4cb648" stroke-width="1.6" fill="none"/></svg></span><div><b>שלח לנו מייל</b><small>info@gadri-example.co.il</small></div></div>

<div class="field" style="left:373px;top:2213px;width:215px">כתובת דוא"ל</div>
<div class="field" style="left:141px;top:2213px;width:214px">שם פרטי</div>
<div class="field" style="left:373px;top:2285px;width:215px">נושא</div>
<div class="field" style="left:141px;top:2285px;width:214px">מספר טלפון</div>
<div class="field" style="left:141px;top:2357px;width:447px">כתובת</div>
<div class="field" style="left:141px;top:2433px;width:447px;height:80px">הקלד את הודעתך כאן</div>
<div class="btn" style="left:481px;top:2535px;width:107px;height:45px">שליחה</div>

<!-- footer -->
<footer class="footer" role="contentinfo">
  <div class="foot-brand"><span>Gadri Management</span><span class="dot"></span></div>
  <p class="foot-text">זהו טקסט דמה לצורך תצוגה בלבד של תוכן האתר העירוני, את התוכן הסופי יספק הלקוח בהמשך העבודה. הטקסט נועד להמחיש את מבנה הפסקה ואת אורך השורות בתחתית הדף</p>

  <h3 style="right:520px;top:92px">קישורים מהירים</h3>
  <span class="foot-link" style="right:529px;top:148px">בית</span>
  <span class="foot-link" style="right:529px;top:190px">אודות</span>
  <span class="foot-link" style="right:529px;top:232px">מיזמי פיתוח</span>
  <span class="foot-link" style="right:529px;top:274px">פרויקטים</span>
  <span class="foot-link" style="right:529px;top:316px">עדכונים</span>
  <span class="foot-link" style="right:644px;top:148px">מכרזים</span>
  <span class="foot-link" style="right:644px;top:190px">מוסדות ציבור</span>
  <span class="foot-link" style="right:644px;top:232px">גלריה</span>
  <span class="foot-link" style="right:644px;top:274px">צור קשר</span>

  <h3 style="right:835px;top:92px">נהיה בקשר</h3>
  <div class="foot-info" style="top:158px"><span class="info-icon"><svg width="18" height="18" viewBox="0 0 16 16" fill="#fff"><path d="M4 1.5l2.2 3.2-1.6 1.5c1 2 2.6 3.6 4.6 4.6l1.5-1.6 3.2 2.2-1 2.6C7 14 2 9 1.5 2.5z"/></svg></span><div><b>התקשר אלינו</b><small>08-9000123</small></div></div>
  <div class="foot-info" style="top:232px"><span class="info-icon"><svg width="16" height="20" viewBox="0 0 16 20" fill="#fff"><path d="M8 0a7 7 0 017 7c0 5-7 13-7 13S1 12 1 7a7 7 0 017-7zm0 4a3 3 0 100 6 3 3 0 000-6z"/></svg></span><div><b>כתובת</b><small>רחוב הדוגמה 12, עיר האלון</small></div></div>
  <div class="foot-info" style="top:300px"><span class="info-icon"><svg width="18" height="14" viewBox="0 0 18 14" fill="#fff"><rect width="18" height="14" rx="2"/><path d="M1 2l8 6 8-6" stroke="#4cb648" stroke-width="1.6" fill="none"/></svg></span><div><b>שלח לנו מייל</b></div></div>
</footer>

<div class="bar">
  <p class="copy">כל הזכויות שמורות &copy;</p>
  <span class="social" style="left:141px"></span>
  <span class="social" style="left:188px"></span>
  <span class="social" style="left:235px"></span>
</div>

</body>
</html>
```